TIDE CREST MARINE Business card

Card for boat detailing business in Bermuda

Target Market(s)

clients. new clients

Industry/Entity Type

Marine

Contact Information for Business Card

TIDE CREST MARINE
Boat Maintenance & Detailing
Dorian K. Halloway
P: 441 972 4617
E: dhalloway@tidecrestmail.net
P.O. Box FL528
Fennick FLBX
Bermuda

Font styles to use
Sans Serif

Colors
85acd3
eaf1f7
0455a3
33b8a4
86cfc6
ffffff
cfdeed

Requirements
Must have
• ALL the information provided. Tropical, water, sky, blue/green/white elements.
Nice to have
• A silhoette of the boat in the photos provided.
Should not have
• Keep it simple and clean. Nothing over the top.

```html
<!DOCTYPE html>
<html lang="en">
<head>
<meta charset="utf-8">
<title>Tide Crest Marine – Business Card</title>
<link rel="stylesheet" href="https://fonts.googleapis.com/css2?family=Cinzel:wght@400;600&family=Lato:wght@400&display=swap">
<style>
  :root {
    --backdrop: #5c5c5c;
    --card-light: #f6f6f6;
    --card-teal: #185c66;
    --ink-teal: #17555f;
    --accent-orange: #d9502a;
    --name-orange: #e2592f;
    --text-light: #eef4f4;
    --rule: rgba(134, 207, 198, 0.35);
  }
  * { margin: 0; padding: 0; box-sizing: border-box; }
  html, body {
    width: 1200px;
    height: 802px;
    overflow: hidden;
    background: var(--backdrop);
  }
  .canvas {
    position: relative;
    width: 1200px;
    height: 802px;
  }
  .card {
    position: absolute;
    top: 274px;
    width: 443px;
    height: 265px;
    box-shadow: 2px 3px 6px rgba(0, 0, 0, 0.45);
    text-align: center;
  }
  .card--front { left: 136px; background: var(--card-light); }
  .card--back { left: 624px; background: var(--card-teal); }

  .brand-name {
    position: absolute;
    left: 0; right: 0;
    top: 98px;
    font-family: "Cinzel", serif;
    font-weight: 600;
    font-size: 31px;
    letter-spacing: 0.5px;
    color: var(--ink-teal);
    line-height: 1;
  }
  .brand-tagline {
    position: absolute;
    left: 0; right: 0;
    top: 148px;
    font-family: "Lato", sans-serif;
    font-size: 13px;
    color: var(--accent-orange);
    line-height: 1;
  }

  .person-name {
    position: absolute;
    left: 0; right: 0;
    top: 74px;
    font-family: "Cinzel", serif;
    font-weight: 400;
    font-size: 28px;
    color: var(--name-orange);
    line-height: 1;
  }
  .rule {
    position: absolute;
    left: 50%;
    width: 170px;
    height: 1px;
    margin-left: -85px;
    background: linear-gradient(90deg, transparent, var(--rule), transparent);
  }
  .rule--top { top: 122px; }
  .rule--bottom { top: 187px; }
  .contact-line {
    position: absolute;
    left: 0; right: 0;
    font-family: "Lato", sans-serif;
    font-size: 16px;
    color: var(--text-light);
    line-height: 1;
  }
  .contact-line--phone { top: 136px; }
  .contact-line--email { top: 156px; }
  .contact-line--address { top: 206px; }
</style>
</head>
<body>
  <main class="canvas">
    <section class="card card--front">
      <h1 class="brand-name">TIDE CREST MARINE</h1>
      <p class="brand-tagline">BOAT MAINTENANCE &amp; DETAILING</p>
    </section>
    <section class="card card--back">
      <h2 class="person-name">Dorian K. Halloway</h2>
      <div class="rule rule--top"></div>
      <p class="contact-line contact-line--phone">441 972 4617</p>
      <p class="contact-line contact-line--email">dhalloway@tidecrestmail.net</p>
      <div class="rule rule--bottom"></div>
      <p class="contact-line contact-line--address">P.O. Box FL528 Fennick FLBX Bermuda</p>
    </section>
  </main>
</body>
</html>
```